Modern Design Business Card industrial maintenance company

Business card design for Company named Brookvale Equipment Services

Target Market(s)

Industrial

Industry/Entity Type

Maintenance and repair

Contact Information for Business Card

Place holder for address, office phone, mobile number and email

Requirements
Must have
• Clean modern look
Nice to have
• N/a

```html
<!DOCTYPE html>
<html lang="en">
<head>
<meta charset="utf-8">
<title>Brookvale Equipment Services – Business Card</title>
<link rel="stylesheet" href="https://fonts.googleapis.com/css2?family=Roboto:wght@400;700&display=swap">
<style>
  :root {
    --canvas: #e9e7e4;
    --card: #ffffff;
    --ink: #0b0b0b;
    --text-soft: #4a4a4a;
    --shadow: rgba(0, 0, 0, 0.18);
  }
  * { box-sizing: border-box; margin: 0; padding: 0; }
  html, body {
    width: 1200px; height: 900px; overflow: hidden;
    background: var(--canvas);
    font-family: "Roboto", Arial, sans-serif;
  }
  .sheet {
    width: 1200px; height: 900px;
    display: flex; flex-direction: column; align-items: center; justify-content: center;
    gap: 36px;
  }
  .card {
    position: relative;
    width: 700px; height: 400px;
    background: var(--card);
    box-shadow: 0 6px 18px var(--shadow);
    overflow: hidden;
  }
  .card__band {
    position: absolute; inset: 0;
    width: 100%; height: 100%;
  }
  .brand {
    position: absolute;
    display: flex; align-items: center; gap: 14px;
    color: var(--ink);
  }
  .brand__mark {
    width: 62px; height: 62px;
    border: 4px solid var(--ink);
    border-radius: 50%;
    flex: none;
  }
  .brand__words {
    display: flex; flex-direction: column;
    font-weight: 700;
    line-height: 1;
  }
  .brand__name {
    font-size: 38px;
    letter-spacing: 2px;
  }
  .brand__tag {
    font-size: 12.5px;
    letter-spacing: 5.2px;
    margin-top: 6px;
  }
  .card--front .brand { left: 300px; top: 150px; }
  .card--back .brand { left: 330px; top: 60px; }

  .contact {
    position: absolute;
    left: 60px; top: 140px;
    color: var(--text-soft);
    font-size: 17px;
    line-height: 1.25;
  }
  .contact__name {
    font-weight: 700;
    font-size: 19px;
    color: var(--ink);
    letter-spacing: 0.2px;
  }
  .contact__role { margin-bottom: 14px; }
  .contact__address { margin-left: 38px; margin-bottom: 14px; }
  .contact__list { list-style: none; margin-left: 60px; }
  .contact__list li {
    display: flex; align-items: center; gap: 10px;
    height: 24px;
  }
  .contact__icon { width: 16px; height: 16px; flex: none; color: var(--ink); }
</style>
</head>
<body>
<main class="sheet">

  <section class="card card--front" aria-label="Card front">
    <svg class="card__band" viewBox="0 0 700 400" preserveAspectRatio="none" aria-hidden="true">
      <polygon points="0,345 235,345 260,362 700,362 700,400 0,400" fill="var(--ink)"/>
    </svg>
    <div class="brand">
      <span class="brand__mark"></span>
      <div class="brand__words">
        <span class="brand__name">BROOKVALE</span>
        <span class="brand__tag">EQUIPMENT SERVICES</span>
      </div>
    </div>
  </section>

  <section class="card card--back" aria-label="Card back">
    <svg class="card__band" viewBox="0 0 700 400" preserveAspectRatio="none" aria-hidden="true">
      <polygon points="0,374 500,374 515,330 700,330 700,400 0,400" fill="var(--ink)"/>
    </svg>
    <div class="brand">
      <span class="brand__mark"></span>
      <div class="brand__words">
        <span class="brand__name">BROOKVALE</span>
        <span class="brand__tag">EQUIPMENT SERVICES</span>
      </div>
    </div>

    <div class="contact">
      <p class="contact__name">ALEX MORGAN</p>
      <p class="contact__role">Director</p>
      <p class="contact__address">00 dummy city<br>dummy place 0000</p>
      <ul class="contact__list">
        <li>
          <svg class="contact__icon" viewBox="0 0 16 16" aria-hidden="true">
            <rect x="4" y="1" width="8" height="14" rx="1.5" fill="none" stroke="currentColor" stroke-width="1.4"/>
            <line x1="7" y1="12.5" x2="9" y2="12.5" stroke="currentColor" stroke-width="1.2"/>
          </svg>
          <span>000-000-0000</span>
        </li>
        <li>
          <svg class="contact__icon" viewBox="0 0 16 16" aria-hidden="true">
            <path d="M3 2l3 0 1 3.5-1.8 1.2a8 8 0 0 0 4.1 4.1L10.5 9 14 10v3a1 1 0 0 1-1 1A11 11 0 0 1 2 3a1 1 0 0 1 1-1z" fill="currentColor"/>
          </svg>
          <span>000-000-0000</span>
        </li>
        <li>
          <svg class="contact__icon" viewBox="0 0 16 16" aria-hidden="true">
            <rect x="1" y="3.5" width="14" height="9.5" rx="0.5" fill="currentColor"/>
            <polyline points="1.5,4 8,9 14.5,4" fill="none" stroke="var(--card)" stroke-width="1.2"/>
          </svg>
          <span>info@brookvale.com</span>
        </li>
      </ul>
    </div>
  </section>

</main>
</body>
</html>
```